https://lanternbrookpaperhouse.org/

We would like the website to represent 19th century African American civil war soldier's letters. We would like the site colors to be nice and clean . Along with the layout, including a great landing page , blogs and introduction.

```html
<!DOCTYPE html>
<html lang="en">
<head>
<meta charset="utf-8">
<title>Lanternbrook Paper House</title>
<link href="https://fonts.googleapis.com/css2?family=Poppins:wght@300;400;500;600;700&display=swap" rel="stylesheet">
<style>
:root{
  --bg:#262626;
  --hero:#2b2b2b;
  --band:#2f2f2f;
  --card:#333333;
  --accent:#e0904c;
  --text:#e6e6e6;
  --muted:#bdbdbd;
  --dim:#8a8a8a;
  --line:#5a5a5a;
}
*{margin:0;padding:0;box-sizing:border-box}
html,body{width:1200px;height:4446px;overflow:hidden}
body{background:var(--bg);font-family:'Poppins',sans-serif;color:var(--text);position:relative}
.abs{position:absolute}
.hero-bg{left:0;top:0;width:1200px;height:785px;background:linear-gradient(180deg,#3a3a3a 0%,#2f2f2f 55%,var(--bg) 100%)}
.brand{left:183px;top:40px;width:160px;text-align:center}
.brand-mark{width:18px;height:18px;border-radius:50%;background:#fff;margin:0 auto 10px}
.brand-name{font-size:18px;font-weight:400;color:#fff;line-height:22px}
.brand-sub{font-size:11px;color:#fff;line-height:16px}
.nav{left:625px;top:66px;display:flex;gap:0;font-size:13px;color:#fff}
.nav span{position:absolute;white-space:nowrap}
.eyebrow{left:185px;top:234px;font-size:12px;letter-spacing:1.5px;color:#fff}
.hero-title{left:183px;top:266px;width:470px;font-size:45px;font-weight:700;line-height:52px;color:#fff}
.meta{display:flex;align-items:center;gap:8px;font-size:12px;letter-spacing:1px;color:#ddd;white-space:nowrap}
.meta .sep{width:1px;height:14px;background:#666;margin:0 8px}
.meta svg{flex:none}
.pager{display:flex;align-items:center;gap:18px}
.pager b{font-size:24px;font-weight:600;color:#fff}
.pager small{font-size:16px;color:#ddd}
.photo{background:linear-gradient(135deg,#8a8a8a,#4a4a4a)}
.social{left:1122px;width:18px}
.social i{display:block;width:10px;height:10px;border-radius:50%;background:#fff;margin:0 auto}
.vline{background:#777}
.h2{font-size:32px;font-weight:700;color:var(--accent);letter-spacing:1px}
.body-text{font-size:13.5px;letter-spacing:1.6px;line-height:25.5px;color:#ddd}
.more{font-size:12px;letter-spacing:1px;color:var(--accent)}
.more::before{content:"";position:absolute;left:0;top:-10px;width:100%;height:1px;background:var(--accent)}
.hr{height:1px;background:var(--line)}
.card{background:var(--card);box-shadow:0 10px 30px rgba(0,0,0,.35)}
.side{background:#2f2f2f}
.side .img{background:linear-gradient(180deg,#7a7a7a,#555)}
.vert{writing-mode:vertical-rl;font-size:22px;color:#aaa;white-space:nowrap}
.tiny{font-size:9px;color:#888}
.band{left:0;top:2524px;width:1200px;height:247px;background:var(--band)}
.input{border:1px solid #777;display:flex;align-items:center}
.quote{text-align:center;font-size:13.5px;letter-spacing:1.6px;line-height:25.5px;color:#ddd}
.contact{left:140px;top:3807px;width:920px;height:515px;background:var(--band);box-shadow:0 10px 40px rgba(0,0,0,.4)}
.map{background:radial-gradient(ellipse at 55% 50%,#3a3a3a 0%,#333 45%,var(--band) 75%)}
.tip{background:#3c3c3c;font-size:8px;color:#ccc;text-align:center;line-height:12px;padding-top:9px}
.foot{left:0;top:4382px;width:1200px;text-align:center;font-size:13px;letter-spacing:1.5px;color:#ddd}
</style>
</head>
<body>

<!-- Hero -->
<div class="abs hero-bg" role="img" aria-label="Dim engraving of mounted soldiers with rifles"></div>
<div class="abs brand"><div class="brand-mark"></div><div class="brand-name">Lanternbrook</div><div class="brand-sub">Paper House</div></div>
<nav class="abs nav" style="left:0;top:66px;width:1200px">
  <span style="left:625px">Home</span><span style="left:694px">About</span><span style="left:763px">Blog</span><span style="left:825px">Contact</span><span style="left:912px">Blog Feed</span>
  <svg style="position:absolute;left:1002px;top:2px" width="15" height="15" viewBox="0 0 16 16" fill="none" stroke="#fff" stroke-width="1.6"><circle cx="7" cy="7" r="5"/><path d="M11 11l4 4"/></svg>
</nav>

<div class="abs eyebrow">PVT. ELIAS ROWAN, 102ND MICHIGAN USCT</div>
<h1 class="abs hero-title">"I'm Well And Doing Well As A Soldier Can Expect..."</h1>
<div class="abs meta" style="left:185px;top:448px">
  <svg width="13" height="13" viewBox="0 0 14 14" fill="#ddd"><circle cx="7" cy="4" r="3"/><path d="M1 14c0-4 3-6 6-6s6 2 6 6z"/></svg>By mbell31<span class="sep"></span>
  <svg width="13" height="13" viewBox="0 0 14 14" fill="#ddd"><rect x="1" y="2" width="12" height="11" rx="1"/></svg>February 16, 2020<span class="sep"></span>
  <svg width="13" height="13" viewBox="0 0 14 14" fill="#ddd"><path d="M7 1C3 1 0 3.5 0 6.5c0 1.8 1 3.3 2.6 4.3L2 14l3.4-2.1c.5.1 1 .1 1.6.1 4 0 7-2.5 7-5.5S11 1 7 1z"/></svg>Comments
</div>
<div class="abs pager" style="left:183px;top:502px">
  <svg width="26" height="12" viewBox="0 0 26 12" fill="none" stroke="#8a5a30" stroke-width="1.5"><path d="M25 6H2M7 1L2 6l5 5"/></svg>
  <div><b>1</b><small>/4</small></div>
  <svg width="26" height="12" viewBox="0 0 26 12" fill="none" stroke="var(--accent)" stroke-width="1.5"><path d="M1 6h23M19 1l5 5-5 5"/></svg>
</div>
<div class="abs" style="left:183px;top:533px;font-size:11px;color:#8a5a30">Prev</div>
<div class="abs" style="left:284px;top:533px;font-size:11px;color:var(--accent);font-weight:600">Next</div>
<div class="abs photo" style="left:679px;top:237px;width:381px;height:250px" role="img" aria-label="Antique keys resting on a worn letter"></div>
<div class="abs vline" style="left:1130px;top:193px;width:1px;height:127px"></div>
<div class="abs social" style="top:358px"><i></i><i style="margin-top:30px"></i><i style="margin-top:30px"></i>
  <svg style="display:block;margin:28px auto 0" width="12" height="9" viewBox="0 0 12 9" fill="#fff"><path d="M0 0h12v9H0z"/><path d="M0 0l6 5 6-5" stroke="#2f2f2f" fill="none"/></svg></div>
<svg class="abs" style="left:587px;top:693px" width="20" height="34" viewBox="0 0 20 34" fill="none" stroke="#ccc" stroke-width="1.5"><rect x="1" y="1" width="18" height="32" rx="9"/><path d="M10 8v6"/></svg>

<!-- About -->
<div class="abs hr" style="left:0;top:979px;width:181px"></div>
<h2 class="abs h2" style="left:197px;top:953px">About Us</h2>
<p class="abs body-text" style="left:197px;top:1018px;width:390px">Marian Okafor Bell is a Virginia native and Maryland-based researcher and scholar. She has received her Ph.D. in English Literature from Harbor State University, her M.A. in English Literature from Crestfield University, and her B.A. in Mass Media Arts from Linwood University. Her areas of specialization include African American Epistolary Literature, African American Civil War letters, nineteenth-century African American and American Literature, and epistolary theory.</p>
<div class="abs more" style="left:499px;top:1334px">Read more</div>
<div class="abs photo" style="left:625px;top:965px;width:378px;height:378px;box-shadow:0 10px 30px rgba(0,0,0,.4)" role="img" aria-label="Portrait of the author wearing glasses"></div>
<div class="abs hr" style="left:1019px;top:981px;width:181px"></div>

<!-- Latest blogs -->
<div class="abs hr" style="left:0;top:1538px;width:181px"></div>
<h2 class="abs h2" style="left:197px;top:1512px">Latest Blogs</h2>
<p class="abs body-text" style="left:197px;top:1570px;width:450px">Lanternbrook Paper House: the lives of and letters from the men of the USCT</p>
<div class="abs hr" style="left:1019px;top:1540px;width:181px"></div>

<div class="abs side" style="left:0;top:1830px;width:136px;height:333px"><div class="abs img" style="left:67px;top:0;width:69px;height:333px" role="img" aria-label="Faded handwritten letter"></div>
  <div class="abs tiny" style="left:16px;top:40px">Feb 20</div><div class="abs" style="left:30px;top:66px;width:1px;height:20px;background:#777"></div>
  <div class="abs vert" style="left:16px;top:105px">Blog Edit Here</div></div>
<div class="abs side" style="left:1063px;top:1830px;width:137px;height:333px"><div class="abs img" style="left:0;top:0;width:70px;height:333px" role="img" aria-label="Faded handwritten letter"></div>
  <div class="abs tiny" style="left:86px;top:40px">Jan 26</div><div class="abs" style="left:104px;top:66px;width:1px;height:20px;background:#777"></div>
  <div class="abs vert" style="left:90px;top:105px">Blog Edit Here</div></div>

<div class="abs photo" style="left:202px;top:1752px;width:416px;height:498px;background:linear-gradient(90deg,#555,#8a8a8a 60%,#bbb)" role="img" aria-label="Weathered stone lion statue"></div>
<article class="abs card" style="left:618px;top:1702px;width:380px;height:588px">
  <div class="abs" style="left:24px;top:62px;font-size:13px;color:#3f3f3f">Latest Blogs</div>
  <h3 class="abs" style="left:24px;top:108px;width:340px;font-size:26px;font-weight:400;line-height:33px;color:#fff;letter-spacing:.5px">"I Have Not Heard From Brother John Since I Wrote To You"</h3>
  <p class="abs body-text" style="left:24px;top:225px;width:340px;font-size:13px">Below is the eighth letter from Pvt. Rowan's collection. Notice in the closing the spelling of his name. It is safe to assume that the soldier who penned Rowan's fifth letter is the same one lending a literal hand three letters later. Crew Saw  S.C Dec 8th/64 Dear Mother I reced your letter 4th [?] [...]</p>
  <div class="abs meta" style="left:24px;top:468px;font-size:9px;gap:6px">
    <svg width="9" height="9" viewBox="0 0 14 14" fill="#ddd"><circle cx="7" cy="4" r="3"/><path d="M1 14c0-4 3-6 6-6s6 2 6 6z"/></svg>By mbell31<span class="sep" style="height:10px"></span>
    <svg width="9" height="9" viewBox="0 0 14 14" fill="#ddd"><rect x="1" y="2" width="12" height="11" rx="1"/></svg>February 16, 2020<span class="sep" style="height:10px"></span>
    <svg width="9" height="9" viewBox="0 0 14 14" fill="#ddd"><circle cx="7" cy="7" r="6"/></svg>Comments</div>
  <div class="abs more" style="left:24px;top:512px">Read more</div>
</article>
<div class="abs pager" style="left:874px;top:2320px">
  <svg width="26" height="12" viewBox="0 0 26 12" fill="none" stroke="#aaa" stroke-width="1.5"><path d="M25 6H2M7 1L2 6l5 5"/></svg>
  <div><b>3</b><small>/4</small></div>
  <svg width="26" height="12" viewBox="0 0 26 12" fill="none" stroke="#fff" stroke-width="1.5"><path d="M1 6h23M19 1l5 5-5 5"/></svg>
</div>

<!-- Follow -->
<section class="abs band"></section>
<h2 class="abs" style="left:199px;top:2625px;font-size:36px;font-weight:300;color:#fff">Follow My Blogs</h2>
<div class="abs" style="left:561px;top:2605px;font-size:13px;color:#fff">Get New Content Delivered Directly To Your Inbox.</div>
<div class="abs input" style="left:561px;top:2645px;width:437px;height:45px">
  <span style="flex:1;padding-left:20px;font-size:11px;letter-spacing:3px;color:#555">EMAIL ADDRESS</span>
  <span style="width:1px;height:28px;background:#777"></span>
  <svg style="margin:0 14px" width="26" height="22" viewBox="0 0 26 22" fill="none" stroke="#fff" stroke-width="1.5"><path d="M1 10L25 1l-6 20-7-8zM25 1L12 13v7"/></svg>
</div>

<!-- Testimonials -->
<h2 class="abs h2" style="left:197px;top:2934px">What People Say</h2>
<div class="abs photo" style="left:167px;top:3042px;width:417px;height:266px" role="img" aria-label="Smiling woman wearing a hat"></div>
<div class="abs" style="left:167px;top:3342px;width:417px;text-align:center;font-size:13px;letter-spacing:1px;color:#ddd">January 16, 2020</div>
<div class="abs" style="left:167px;top:3384px;width:417px;text-align:center;font-size:22px;letter-spacing:1px;color:#fff">Nora Whitfield</div>
<p class="abs quote" style="left:187px;top:3473px;width:377px">"We all grow up with the weight of history on us. Our ancestors dwell in the attics of our brains as they do in the spiraling chains of hidden knowledge in every cell of our bodies."</p>
<div class="abs photo" style="left:623px;top:2954px;width:416px;height:266px" role="img" aria-label="Archival portrait of a woman in a hat"></div>
<div class="abs" style="left:623px;top:3254px;width:416px;text-align:center;font-size:13px;letter-spacing:1px;color:#ddd">January 28, 2020</div>
<div class="abs" style="left:623px;top:3296px;width:416px;text-align:center;font-size:22px;letter-spacing:1px;color:#fff">Ada Louise Carver</div>
<p class="abs quote" style="left:643px;top:3385px;width:376px">"We all grow up with the weight of history on us. Our ancestors dwell in the attics of our brains as they do in the spiraling chains of hidden knowledge in every cell of our bodies."</p>
<div class="abs more" style="left:953px;top:3599px">All Posts</div>

<!-- Contact -->
<section class="abs contact">
  <div class="abs map" style="left:370px;top:80px;width:550px;height:400px" role="img" aria-label="Dotted world map"></div>
  <div class="abs tip" style="left:613px;top:69px;width:103px;height:55px">Waiting For You<br>Here</div>
  <div class="abs" style="left:662px;top:139px;width:6px;height:6px;border-radius:50%;background:#fff"></div>
  <h2 class="abs h2" style="left:43px;top:130px">Stay In Touch</h2>
  <p class="abs body-text" style="left:43px;top:190px;width:280px">Let's talk Don't hesitate to reach out with the contact information below, or send a message using the form.</p>
  <div class="abs" style="left:43px;top:314px;display:flex;align-items:center;gap:10px;font-size:13.5px;letter-spacing:1.6px;color:#ddd">
    <svg width="12" height="9" viewBox="0 0 12 9" fill="#ddd"><path d="M0 0h12v9H0z"/><path d="M0 0l6 5 6-5" stroke="#2f2f2f" fill="none"/></svg>marian.bell@lanternbrook.org</div>
  <div class="abs more" style="left:43px;top:380px">Contact me</div>
</section>

<footer class="abs foot">© 2020 Lanternbrook Paper House</footer>
</body>
</html>
```